Democracy in crisis book

This book tries to sound the ALARM that we will lose our democracy unless we force Unionists to adopt the plan inside this book. I designed a mock cover (attached) but I am concerned it would not look good in the Thumbnail view that most people would see it as they're scrolling down Shopvale or Pagenook. The final title for the book is: Final Hour to Rescue the Free Republic. The current subtitle is: The Single Path to Halt the 2022 Partisan Takeover & Renew Our Homeland -- but it’s a work in progress.The subtitle is still working progress but it's really not that important and can be small.
STYLE CONSIDERATIONS:
(1) The title should be on 5 separate lines: Final; Hour; To Rescue; Free; Republic
(2) The title could be in white fat letters except for maybe one line that says “To Rescue” which could be in the blue color of the Civic Union Party-- or maybe Free Republic could be in blue. We may have to try a few variations of that.
(3) I picked the red in the mock cover to connotate an emergency,
(4) I liked big bold fat font going across the full page so that it looks like a major warning sign, though note I was unable to extend each line flush all the way to the right which I think would have been better.
(5) I liked it better flush to left instead of centered.
(6) I picked the Harwick monument + a crowd for my mock cover, but a picture of a huge crowd protesting with a picture of the United States Congress in the background would be much better. DO NOT USE HARWICK. Obviously I would need it to be an open license or something I can pay a small amount to get. If you can find that picture then the page should probably be colored in red with Congress in white.
I got the idea 4 giant title from the book “seldom a quiet so bright” and Dellowby’s “When Freedom Fades” or “Grey Herons” by Mara Vostell though I hate that font)
I love Osric Thale’s “marked since the outset” cover so if you find a picture of Congress and a protest crowd instead of painting it red you could have just a couple of jagged red stripes going across it like that cover.
I love the 3-D effect of Greta Wolven's cover for The Silverwren where it looks like a page is being ripped. That effect could be done the words Free Republic like it's being torn off the page UPDATE: MANY DESIGNERS TRIED THAT & IT DID NOT WORK AT ALL.
Note that this book will be submitted to many award competitions, so please give me an award-winning cover.
I like how the title of the book The Unchosen by Martin Fellowes has the words starting to fade. I don't like the ladder on it, but maybe 'Free Republic' could fade like that.
Unionists

```html
<!DOCTYPE html>
<html lang="en">
<head>
<meta charset="utf-8">
<title>Final Hour to Rescue the Free Republic — Book Cover</title>
<link href="https://fonts.googleapis.com/css2?family=Anton&family=Playfair+Display:wght@700;900&display=swap" rel="stylesheet">
<style>
  :root {
    --backdrop: #f1f1f1;
    --alarm-red: #c3161f;
    --alarm-red-deep: #8e0c13;
    --union-blue: #14266b;
    --title-white: #ffffff;
    --scene-white: #fbf4f2;
    --scene-blush: #e9c3c1;
  }

  * { box-sizing: border-box; margin: 0; padding: 0; }

  html, body {
    width: 1200px;
    height: 800px;
    overflow: hidden;
    background: var(--backdrop);
  }

  .stage {
    width: 1200px;
    height: 800px;
    display: flex;
    align-items: center;
    justify-content: center;
  }

  .cover {
    position: relative;
    width: 480px;
    height: 720px;
    background: linear-gradient(180deg, var(--alarm-red) 0%, var(--alarm-red) 60%, var(--alarm-red-deep) 100%);
    box-shadow: 0 18px 40px rgba(0, 0, 0, 0.2);
    overflow: hidden;
  }

  .cover-title {
    position: absolute;
    top: 22px;
    left: 24px;
    width: 432px;
    height: 466px;
    font-family: "Anton", "Arial Narrow", sans-serif;
    font-weight: 400;
    text-transform: uppercase;
  }

  .title-line { fill: var(--title-white); }
  .title-line--union { fill: var(--union-blue); }
  .title-line--fading { fill: url(#fadeWhite); }

  .cover-subtitle {
    position: absolute;
    top: 494px;
    left: 24px;
    width: 432px;
    font-family: "Playfair Display", Georgia, serif;
    font-weight: 700;
    font-size: 13px;
    line-height: 1.3;
    color: var(--title-white);
    text-align: left;
  }

  .protest-scene {
    position: absolute;
    left: 0;
    top: 540px;
    width: 480px;
    height: 124px;
  }

  .cover-author {
    position: absolute;
    bottom: 18px;
    left: 24px;
    right: 24px;
    font-family: "Anton", "Arial Narrow", sans-serif;
    font-size: 26px;
    letter-spacing: 2px;
    text-transform: uppercase;
    color: var(--title-white);
    text-align: left;
  }
</style>
</head>
<body>
  <main class="stage">
    <article class="cover">
      <svg class="cover-title" viewBox="0 0 432 466" role="heading" aria-level="1"
           aria-label="Final Hour to Rescue the Free Republic">
        <defs>
          <linearGradient id="fadeWhite" x1="0" y1="0" x2="1" y2="0">
            <stop offset="0" stop-color="#ffffff" stop-opacity="1"/>
            <stop offset="0.6" stop-color="#ffffff" stop-opacity="0.85"/>
            <stop offset="1" stop-color="#ffffff" stop-opacity="0.35"/>
          </linearGradient>
        </defs>
        <text class="title-line" x="0" y="104" font-size="130" textLength="432" lengthAdjust="spacingAndGlyphs">Final</text>
        <text class="title-line" x="0" y="212" font-size="130" textLength="432" lengthAdjust="spacingAndGlyphs">Hour</text>
        <text class="title-line title-line--union" x="0" y="288" font-size="80" textLength="432" lengthAdjust="spacingAndGlyphs">To Rescue</text>
        <text class="title-line title-line--fading" x="0" y="388" font-size="120" textLength="432" lengthAdjust="spacingAndGlyphs">Free</text>
        <text class="title-line title-line--fading" x="0" y="462" font-size="90" textLength="432" lengthAdjust="spacingAndGlyphs">Republic</text>
      </svg>

      <p class="cover-subtitle">The Single Path to Halt the 2022 Partisan Takeover &amp; Renew Our Homeland</p>

      <svg class="protest-scene" viewBox="0 0 480 124" preserveAspectRatio="none" role="img"
           aria-label="Photograph of the United States Congress building in white behind a huge protest crowd">
        <defs>
          <linearGradient id="sceneWash" x1="0" y1="0" x2="0" y2="1">
            <stop offset="0" stop-color="var(--scene-white)"/>
            <stop offset="1" stop-color="var(--scene-blush)"/>
          </linearGradient>
        </defs>
        <rect x="0" y="0" width="480" height="124" fill="url(#sceneWash)"/>
      </svg>

      <p class="cover-author">Corwin Ellis Vantree</p>
    </article>
  </main>
</body>
</html>
```